Flyer Design For Building & Decorating Company

We need an A6 double-sided colour flyer for a letter-box marketing campaign. We are a building and decorating company based in West London. We saw a flyer that we liked and have attached it as an example of the sort of thing we're looking for (see attached files Example A6 Flyer - Front.png and Example A6 Flyer - Back.png). Please note that we're not expecting the designer to slavishly follow this design, more to use it as a jumping-off point.

The design must incorporate a strong call to action, e.g., Call Us For A Free, No-Obligation Quote.

The textual information that must be included in the flyer (contact methods, tagline, services, etc.) are included in the attached file Flyer Text.docx.

Also included as attachments are a selection of images used on our website (files bathroom.png, carpentry.png, decorating.jpg,
flooring.jpg, painting_decorating.jpg, repointing.jpg and work_ on_scaffold.jpg). Please include these images on the flyer (at least one image on each side), or use stock images if any of these are unsuitable.

The company logo will also need to be included in the flyer - see attached file logo.png

The images on our website have all had to be re-sized from the originals. I've attached a number of the original images to this brief, as these are the highest resolution versions of the images that we have. I would ask that you use the versions attached to the brief, but if you feel that other images from our website would work better on your flyer design, please let me know and I'll attach them to this brief.

Finally, we've attached guideline notes from our printer (see attached file Printer's Requirements.docx) - please ensure these are adhered to where relevant.

Target Market(s)

People in West London who require building or decorating work to be done on their properties.

Industry/Entity Type

Marketing

Requirements
Must have
• A6 double-sided colour flyer using the text we provided and some of the images provided.

The call to action must be prominent and eye-catching, as the only purpose of the flyer is to get recipients to contact our company for a quote.

```html
<!DOCTYPE html>
<html lang="en">
<head>
<meta charset="utf-8">
<title>Oakline Renovations – A6 Flyer</title>
<link rel="stylesheet" href="https://fonts.googleapis.com/css2?family=PT+Sans:ital,wght@0,400;0,700;1,400;1,700&family=Kalam:wght@300;400&display=swap">
<style>
  :root {
    --canvas: #ffffff;
    --paper: #fbfaf1;
    --paper-edge: #e6e3cf;
    --olive: #a39a45;
    --olive-dark: #7d7630;
    --olive-light: #c6bf7d;
    --band: #cbc48f;
    --ink: #3d3d3d;
    --ink-soft: #6b6b6b;
    --list: #5c6a55;
    --tick: #4a4a4a;
  }
  * { box-sizing: border-box; margin: 0; padding: 0; }
  html, body { width: 1200px; height: 906px; overflow: hidden; background: var(--canvas); }
  body { position: relative; font-family: "PT Sans", Arial, sans-serif; color: var(--ink); }

  .flyer-side {
    position: absolute; top: 98px; width: 538px; height: 758px;
    background: linear-gradient(180deg, var(--paper) 0%, #f6f3e2 100%);
    border: 1px solid var(--paper-edge);
    overflow: hidden;
  }
  .flyer-front { left: 32px; }
  .flyer-back { left: 641px; }

  .photo { position: absolute; border: 1px solid #8a8a7a; }

  /* Front */
  .brand {
    position: absolute; left: 34px; top: 34px; width: 110px;
    display: flex; flex-direction: column; align-items: center; gap: 6px;
  }
  .brand-mark { width: 22px; height: 22px; background: var(--olive); }
  .brand-name { font-size: 15px; font-weight: 700; color: var(--olive-dark); text-align: center; line-height: 1.1; }

  .headline { position: absolute; left: 150px; top: 26px; width: 370px; text-align: center; }
  .headline h1 {
    font-size: 31px; line-height: 1.05; font-weight: 700; color: var(--olive);
    letter-spacing: -0.3px;
  }
  .tagline { margin-top: 6px; font-size: 17px; font-style: italic; color: var(--ink-soft); letter-spacing: 1.2px; }

  .service-grid {
    position: absolute; left: 62px; top: 462px; width: 420px;
    display: grid; grid-template-columns: 1fr 1fr; row-gap: 1px; column-gap: 16px;
    list-style: none;
  }
  .service-grid li, .service-group li.heading {
    font-family: "Kalam", "Comic Sans MS", cursive; font-style: italic;
  }
  .service-grid li { font-size: 16px; color: var(--list); display: flex; align-items: center; gap: 8px; }
  .tick { width: 16px; height: 14px; flex: none; }

  .call-to-action {
    position: absolute; left: 0; top: 618px; width: 100%; text-align: center;
    font-size: 33px; line-height: 1.12; font-weight: 700; color: #5d6468; letter-spacing: -0.5px;
  }

  .contact-band {
    position: absolute; left: 0; bottom: 0; width: 100%; height: 66px;
    background: var(--band); text-align: center; padding-top: 8px;
  }
  .contact-web { font-size: 21px; font-weight: 700; color: #333; }
  .contact-lines { font-size: 9px; color: #3a3a3a; line-height: 1.35; }

  /* Back */
  .service-group { position: absolute; left: 16px; width: 290px; list-style: none; }
  .service-group .heading {
    display: flex; align-items: flex-end; gap: 6px;
    font-size: 21px; color: var(--olive); line-height: 1; margin-bottom: 4px;
  }
  .service-group .heading .tick { width: 24px; height: 22px; }
  .service-group .item {
    font-family: "Kalam", "Comic Sans MS", cursive; font-style: italic;
    font-size: 12.5px; color: #333; line-height: 1.22; padding-left: 34px; position: relative;
  }
  .service-group .item::before { content: "•"; position: absolute; left: 24px; }
</style>
</head>
<body>

<svg width="0" height="0" style="position:absolute">
  <defs>
    <symbol id="tick" viewBox="0 0 16 14">
      <path d="M1 7.5 L6 12.5 L15 1.5" fill="none" stroke="currentColor" stroke-width="2.2" stroke-linecap="round" stroke-linejoin="round"/>
    </symbol>
  </defs>
</svg>

<section class="flyer-side flyer-front" aria-label="Flyer front">
  <div class="brand">
    <span class="brand-mark"></span>
    <span class="brand-name">Oakline Renovations</span>
  </div>

  <header class="headline">
    <h1>West London<br>Builders &amp; Decorators</h1>
    <p class="tagline">Quality Renovations At Affordable Prices</p>
  </header>

  <div class="photo" role="img" aria-label="Carpenter building a wooden cabinet frame" style="left:32px;top:158px;width:213px;height:137px;background:linear-gradient(135deg,#c9a57a,#8e6a48 60%,#5b4a3c)"></div>
  <div class="photo" role="img" aria-label="Worker laying block paving" style="left:250px;top:158px;width:255px;height:137px;background:linear-gradient(160deg,#8f9a7a,#6d7a5e 55%,#9a8f7c)"></div>
  <div class="photo" role="img" aria-label="Hands fitting laminate flooring" style="left:32px;top:304px;width:143px;height:140px;background:linear-gradient(135deg,#c39a62,#a07444 60%,#6e5236)"></div>
  <div class="photo" role="img" aria-label="Bathroom with blue tiled wall and radiator" style="left:181px;top:304px;width:146px;height:140px;background:linear-gradient(160deg,#3e5d8a,#6f8fb4 55%,#d8d8d3)"></div>
  <div class="photo" role="img" aria-label="Room being stripped for plastering and decoration" style="left:333px;top:304px;width:172px;height:140px;background:linear-gradient(150deg,#b69e7c,#8d7a5f 55%,#c9b89a)"></div>

  <ul class="service-grid">
    <li><svg class="tick" style="color:var(--olive)"><use href="#tick"/></svg>Bathroom / Kitchen</li>
    <li><svg class="tick" style="color:var(--olive)"><use href="#tick"/></svg>Flooring</li>
    <li><svg class="tick" style="color:var(--olive)"><use href="#tick"/></svg>Tiling</li>
    <li><svg class="tick" style="color:var(--olive)"><use href="#tick"/></svg>Plumbing</li>
    <li><svg class="tick" style="color:var(--olive)"><use href="#tick"/></svg>Painting / Decorating</li>
    <li><svg class="tick" style="color:var(--olive)"><use href="#tick"/></svg>Electrical Works</li>
    <li><svg class="tick" style="color:var(--olive)"><use href="#tick"/></svg>Plastering</li>
    <li><svg class="tick" style="color:var(--olive)"><use href="#tick"/></svg>Brickwork</li>
    <li><svg class="tick" style="color:var(--olive)"><use href="#tick"/></svg>Carpentry</li>
    <li><svg class="tick" style="color:var(--olive)"><use href="#tick"/></svg>General Repairs</li>
  </ul>

  <p class="call-to-action">Call Us For A Free,<br>No-Obligation Quote.</p>

  <footer class="contact-band">
    <p class="contact-web">www.oakline-renovations.co.uk</p>
    <p class="contact-lines">Address: Oakline Renovations 14 Larchfield Road, Ealing, London W5 0AA<br>
      Tel: 020 7946 0123 &nbsp; Mobile: 07700 900123 &nbsp; hello@oakline-renovations.co.uk</p>
  </footer>
</section>

<section class="flyer-side flyer-back" aria-label="Flyer back">
  <ul class="service-group" style="top:36px">
    <li class="heading"><svg class="tick" style="color:var(--tick)"><use href="#tick"/></svg>Bathroom / Kitchen</li>
    <li class="item">Complete/Partial Fixings</li>
    <li class="item">Tiling</li>
    <li class="item">Sink/Bath/Radiator</li>
    <li class="item">Tap Repairs/Replace</li>
    <li class="item">Fit Washing Machine/Dishwasher</li>
  </ul>

  <ul class="service-group" style="top:158px">
    <li class="heading"><svg class="tick" style="color:var(--tick)"><use href="#tick"/></svg>Decorating</li>
    <li class="item">Complete/Partial Works</li>
    <li class="item">Lining/Wallpaper</li>
    <li class="item">Painting Inside/Outside</li>
    <li class="item">Plastering/Skimming</li>
    <li class="item">Rectify Damage/Freshen Paintwork</li>
  </ul>

  <ul class="service-group" style="top:286px">
    <li class="heading"><svg class="tick" style="color:var(--tick)"><use href="#tick"/></svg>Carpentry</li>
    <li class="item">Wardrobes/Cupboards</li>
    <li class="item">Shelving/Skirting</li>
    <li class="item">Doors/Windows</li>
    <li class="item">Kitchen/Bathroom Suites</li>
    <li class="item">Wooden Floor/Laminate</li>
  </ul>

  <ul class="service-group" style="top:410px">
    <li class="heading"><svg class="tick" style="color:var(--tick)"><use href="#tick"/></svg>Maintenance / Repairs</li>
    <li class="item">Reseal Bath/Shower</li>
    <li class="item">Fit Shelves</li>
    <li class="item">Electrics - Complete/Partial</li>
    <li class="item">Sash/Gutter/Roof Repairs</li>
    <li class="item">Lots more ...</li>
  </ul>

  <ul class="service-group" style="top:534px">
    <li class="heading"><svg class="tick" style="color:var(--tick)"><use href="#tick"/></svg>Landscaping / Roof /</li>
    <li class="heading" style="padding-left:30px">Work on High Ladders</li>
    <li class="item">Fencing/Paving/Decking</li>
    <li class="item">Work on High Ladders/Scaffold</li>
    <li class="item">Tree Cutting/Removal</li>
    <li class="item">Roofing - New/Repair</li>
  </ul>

  <div class="photo" role="img" aria-label="White house front wrapped in scaffolding" style="left:304px;top:45px;width:143px;height:283px;background:linear-gradient(180deg,#aebfd6 0%,#e9ebe6 30%,#c7c3b9 70%,#8e8a80 100%)"></div>
  <div class="photo" role="img" aria-label="Close-up of freshly repointed red brick wall" style="left:304px;top:342px;width:143px;height:240px;background:linear-gradient(135deg,#b8543a,#9a3f2a 50%,#c06a4e)"></div>

  <footer class="contact-band">
    <p class="contact-web">www.oakline-renovations.co.uk</p>
    <p class="contact-lines">Address: Oakline Renovations 14 Larchfield Road, Ealing, London W5 0AA<br>
      Tel: 020 7946 0123 &nbsp; Mobile: 07700 900123 &nbsp; hello@oakline-renovations.co.uk</p>
  </footer>
</section>

</body>
</html>
```